Logo & Visitenkarte für Soziale Dienstleistungen, Beratung & Therapie
Zielgruppe
[frontside]
Konrad Wallmuth
Dipl. Sozialpädagoge (FH)
systemischer Einzel-, Paar- und Familientherapeut (VKTB)
Mobil: 0176 / 4 829 31 57
Mail: konrad-wallmuth@rundpost.de
'Soziale Dienstleistungen, Beratung & Therapie' [slogan]
[social services, counseling & therapy]
'systemische Beratung & Therapie,
ambulante Hilfen zur Erziehung, intensive Familienberatung, aufsuchende Familientherapie
soziale Projekte, Erwachsenenbildung, Lehraufträge' [business offers - backside of the card]
Zielgruppen [traget groups]:
Familien, Kinder- und Jugendliche, Einzelpersonen, Netzwerkpartner,
Institutionen, Ämter, Schulen, Kliniken, etc.

```html
<!DOCTYPE html>
<html lang="de">
<head>
<meta charset="utf-8">
<title>Konrad Wallmuth – Visitenkarte</title>
<link rel="stylesheet" href="https://fonts.googleapis.com/css2?family=Encode+Sans+Semi+Condensed:wght@300;600&display=swap">
<style>
  :root {
    --backdrop: #efe1c4;
    --paper: #ffffff;
    --teal: #5e8d87;
    --teal-text: #4f8a80;
    --sage: #86b08f;
    --leaf: #a3d39a;
    --ink: #3f4a48;
  }
  * { margin: 0; padding: 0; box-sizing: border-box; }
  html, body { width: 800px; height: 1200px; overflow: hidden; }
  body {
    background: var(--backdrop);
    font-family: "Encode Sans Semi Condensed", "Arial Narrow", sans-serif;
    color: var(--ink);
    position: relative;
  }
  .card {
    position: absolute;
    top: 353px;
    width: 320px;
    height: 493px;
  }
  .card-front { left: 50px; background: var(--paper); }
  .card-back {
    left: 430px;
    background: var(--teal);
    display: flex;
    align-items: center;
    justify-content: center;
  }
  .brand-dot {
    position: absolute;
    left: 30px;
    top: 60px;
    width: 30px;
    height: 30px;
    border-radius: 50%;
    background: var(--teal);
  }
  .brand-name {
    position: absolute;
    left: 97px;
    top: 53px;
    font-weight: 600;
    font-size: 20px;
    color: var(--ink);
  }
  .slogan {
    position: absolute;
    left: 97px;
    top: 96px;
    font-weight: 300;
    font-size: 19px;
    line-height: 24px;
    color: var(--ink);
  }
  .contact {
    position: absolute;
    left: 29px;
    top: 297px;
    font-weight: 300;
    font-size: 16px;
    line-height: 20px;
  }
  .contact-name {
    font-weight: 600;
    color: var(--teal-text);
    margin-bottom: 1px;
  }
  .contact-lines { margin-top: 10px; }
  .contact-line { display: flex; align-items: center; gap: 13px; }
  .contact-line svg { width: 15px; height: 15px; flex: none; }
  .back-name {
    font-weight: 600;
    font-size: 30px;
    color: var(--leaf);
  }
</style>
</head>
<body>
  <section class="card card-front">
    <span class="brand-dot"></span>
    <div class="brand-name">Konrad Wallmuth</div>
    <div class="slogan">Soziale Dienstleistungen,<br>Beratung &amp; Therapie</div>
    <div class="contact">
      <div class="contact-name">Konrad Wallmuth</div>
      <div>Dipl. Sozialpädagoge (FH)<br>systemischer Einzel-, Paar-<br>und Familientherapeut (VKTB)</div>
      <div class="contact-lines">
        <div class="contact-line">
          <svg viewBox="0 0 16 16" aria-hidden="true"><rect x="4" y="1" width="8" height="14" rx="1.5" fill="none" stroke="var(--teal-text)" stroke-width="1.3"/><line x1="7" y1="12.5" x2="9" y2="12.5" stroke="var(--teal-text)" stroke-width="1.3"/></svg>
          <span>0176 / 4 829 31 57</span>
        </div>
        <div class="contact-line">
          <svg viewBox="0 0 16 16" aria-hidden="true"><rect x="1" y="3.5" width="14" height="10" rx="1.5" fill="none" stroke="var(--teal-text)" stroke-width="1.3"/><polyline points="1.5,4.5 8,9.5 14.5,4.5" fill="none" stroke="var(--teal-text)" stroke-width="1.3"/></svg>
          <span>konrad-wallmuth@rundpost.de</span>
        </div>
      </div>
    </div>
  </section>

  <section class="card card-back">
    <span class="back-name">Konrad Wallmuth</span>
  </section>
</body>
</html>
```